Brimlock - a software development company requires letter head

I currently have a business card and logo, I just need a nice looking letter head the matches the two. I will upload these Illustrator files.

I would like the letter head to be done in a current version of MS Word.

Please incorporate 'brimlock' as per the attached font and the logo.

Industry/Entity Type

Computer Software

Colors

Designer to choose colors to be used in the design.

Requirements
Must have
• Fits in with current design, sleek and professional. It will be used for quotations and tenders and documentation going to clients and potential clients.
• Would like to company logo up the top header and perhaps a watermark of the logo at the bottom right, a bit like the business card.
• Also it needs to be MS word.
• Please work with the color pallet from the attached files.

```html
<!DOCTYPE html>
<html lang="en">
<head>
<meta charset="utf-8">
<title>Brimlock Letterhead</title>
<link href="https://fonts.googleapis.com/css2?family=Open+Sans:wght@400;600&display=swap" rel="stylesheet">
<style>
  :root {
    --backdrop: #ececec;
    --paper: #ffffff;
    --ink: #4a4a4a;
    --brand-blue: #2ea3dc;
    --watermark-blue: #dcecf6;
  }
  html, body {
    margin: 0;
    padding: 0;
    width: 1200px;
    height: 1006px;
    overflow: hidden;
    background: var(--backdrop);
    font-family: "Open Sans", sans-serif;
  }
  .letterhead {
    position: absolute;
    left: 229px;
    top: 24px;
    width: 742px;
    height: 957px;
    background: var(--paper);
    overflow: hidden;
    box-shadow: 0 2px 10px rgba(0,0,0,0.12);
  }
  .brand {
    position: absolute;
    left: 83px;
    top: 112px;
    display: flex;
    align-items: center;
    gap: 10px;
  }
  .brand-dot {
    width: 20px;
    height: 20px;
    border-radius: 50%;
    background: var(--brand-blue);
  }
  .brand-name {
    font-family: "Open Sans", sans-serif;
    font-weight: 600;
    font-size: 24px;
    letter-spacing: 1.5px;
    color: var(--ink);
    text-transform: uppercase;
  }
  .contact {
    position: absolute;
    left: 570px;
    top: 82px;
    font-size: 9.5px;
    line-height: 12px;
    color: var(--ink);
  }
  .contact-address { margin: 0 0 9px; font-style: normal; }
  .contact-list { list-style: none; margin: 0; padding: 0; }
  .contact-list li { display: flex; align-items: center; gap: 6px; }
  .contact-icon { width: 8px; height: 8px; flex: none; }
  .watermark {
    position: absolute;
    left: 430px;
    top: 690px;
    width: 380px;
    height: 380px;
    border-radius: 50%;
    background: var(--watermark-blue);
    opacity: 0.8;
  }
</style>
</head>
<body>
  <main class="letterhead">
    <header>
      <div class="brand">
        <span class="brand-dot"></span>
        <span class="brand-name">Brimlock</span>
      </div>
      <div class="contact">
        <address class="contact-address">14 Harlow Lane, Unit 3<br>Westfield Park, CA 90210.</address>
        <ul class="contact-list">
          <li>
            <svg class="contact-icon" viewBox="0 0 10 10" aria-hidden="true"><path d="M2 1 L4 1 L4.6 3.2 L3.4 4 Q4.4 6 6 6.6 L6.8 5.4 L9 6 L9 8 Q9 9 8 9 Q1 8.6 1 2 Q1 1 2 1Z" fill="var(--brand-blue)"/></svg>
            <span>+1 555 014 2288</span>
          </li>
          <li>
            <svg class="contact-icon" viewBox="0 0 10 10" aria-hidden="true"><rect x="1" y="2.5" width="8" height="5.5" rx="0.6" fill="none" stroke="var(--brand-blue)" stroke-width="1.2"/><path d="M1.3 3 L5 5.8 L8.7 3" fill="none" stroke="var(--brand-blue)" stroke-width="1.1"/></svg>
            <span>hello@brimlock.dev</span>
          </li>
          <li>
            <svg class="contact-icon" viewBox="0 0 10 10" aria-hidden="true"><circle cx="5" cy="5" r="3.8" fill="none" stroke="var(--brand-blue)" stroke-width="1.1"/><path d="M1.2 5 H8.8 M5 1.2 Q2.8 5 5 8.8 M5 1.2 Q7.2 5 5 8.8" fill="none" stroke="var(--brand-blue)" stroke-width="0.8"/></svg>
            <span>www.brimlock.dev</span>
          </li>
        </ul>
      </div>
    </header>
    <div class="watermark" aria-hidden="true"></div>
  </main>
</body>
</html>
```